Tri-fold Brochure for Law Firm

Double-sided brochure to be folded into 6 sides tri-fold brochure for an estate planning special for new parents or parents-to-be. Brochure will be placed in classes for new parents/young parents.

Target Market(s)

New Parents Aged 24-34

Industry/Entity Type

Law Firm

Font styles to use
Serif

Requirements
Must have
• The information provided in the word document.
Nice to have
• Highlight the phrase "for New Parents."
• You may use the color scheme from our website:
• http://k47.9dw.sitevaultexample.com/

```html
<!DOCTYPE html>
<html lang="en">
<head>
<meta charset="utf-8">
<title>Hollins Legal — Estate Planning Special for New Parents</title>
<link href="https://fonts.googleapis.com/css2?family=Arimo:wght@400;700&family=Libre+Baskerville:wght@400;700&display=swap" rel="stylesheet">
<style>
  :root{
    --wine:#8c2a27;
    --wine-dark:#6f1f1d;
    --rose:#d3545a;
    --rose-soft:#dc6a6f;
    --gold:#f0bd3a;
    --gold-text:#f7d34f;
    --paper:#ffffff;
    --ink:#1d1d1d;
    --ground:#e6e6e6;
  }
  *{box-sizing:border-box;margin:0;padding:0}
  html,body{width:916px;height:1200px;overflow:hidden;background:var(--ground)}
  body{position:relative;font-family:"Arimo",Arial,sans-serif;color:var(--ink)}
  .sheet{position:absolute;left:87px;width:741px;height:572px;display:flex;box-shadow:0 6px 18px rgba(0,0,0,.18)}
  .sheet--outside{top:20px}
  .sheet--inside{top:608px}
  .panel{position:relative;width:247px;height:572px;overflow:hidden;background:var(--paper)}
  .photo{position:absolute;left:0;right:0}
  .body-text{font-size:7.6px;line-height:1.38}
  .body-text p+p{margin-top:6px}

  /* outside: inner flap */
  .flap__photo{top:0;height:78px;background:linear-gradient(160deg,#5a5a5a 0%,#c9b48a 35%,#ffffff 70%)}
  .flap__content{position:absolute;top:96px;left:20px;right:18px}
  .flap__title{font-family:"Arimo",Arial,sans-serif;font-size:14.5px;font-weight:700;color:var(--wine);margin-bottom:10px;white-space:nowrap}
  .flap__list{margin-top:10px;padding-left:12px;font-size:7.6px;line-height:1.5}
  .flap__band{position:absolute;left:0;right:0;bottom:0;height:62px;background:var(--wine);display:flex;align-items:center;justify-content:center}
  .flap__url{color:#fff;font-weight:700;font-size:11px}

  /* outside: back panel */
  .back__photo{top:0;height:360px;background:linear-gradient(180deg,#6fa6d6 0%,#bcd8ef 45%,#e6f0f8 70%,#2a2a2a 100%)}
  .back__block{position:absolute;left:0;right:0;bottom:0;height:212px;background:var(--gold);padding:40px 12px 0;text-align:center;color:#fff}
  .brand{font-family:"Libre Baskerville",Georgia,serif;font-size:13px;letter-spacing:1px;color:#fff;display:flex;align-items:center;justify-content:center;gap:8px;white-space:nowrap}
  .brand__mark{width:8px;height:8px;border-radius:50%;background:#fff;flex:none}
  .back__contact{margin-top:14px;font-size:7.6px;line-height:1.55;font-style:normal}

  /* outside: cover */
  .cover{background:var(--wine)}
  .cover__art{position:absolute;inset:0}
  .cover__tagline{position:absolute;left:0;right:0;bottom:128px;text-align:center;color:#fff;font-size:9.5px}
  .cover__tagline em{font-style:normal;color:var(--gold-text);font-weight:700;font-size:11px}

  /* inside */
  .top-bar{position:absolute;top:0;left:0;right:0;height:12px;background:var(--rose)}
  .offer{position:absolute;top:30px;left:14px;right:14px;text-align:center}
  .offer__head{font-family:"Libre Baskerville",Georgia,serif;color:var(--rose);font-size:9px;font-weight:700}
  .offer__price{display:inline-block;margin:9px 0;background:var(--rose);color:#fff;font-family:"Libre Baskerville",Georgia,serif;font-weight:700;font-size:12px;padding:4px 10px}
  .offer__who{color:var(--rose);font-size:9.5px;font-weight:700;line-height:1.3}
  .gavel__photo{top:140px;height:118px;background:linear-gradient(135deg,#5b3a1c 0%,#c08236 40%,#e7b25b 60%,#8a5a2a 100%)}
  .red-block{position:absolute;left:0;right:0;background:var(--rose);color:#fff;padding:14px 16px}
  .red-block--low{top:258px;bottom:0}
  .red-block--high{top:12px;height:200px;padding-top:16px}
  .q{font-weight:700;color:var(--gold-text);font-size:9px;margin:10px 0 5px}
  .q:first-child{margin-top:0}
  .q--rose{color:var(--rose);font-size:10px}
  .white-block{position:absolute;left:16px;right:16px;top:224px}
  .scales__photo{bottom:0;height:120px;background:linear-gradient(160deg,#6b3b1b 0%,#c9853e 35%,#f2d5a0 55%,#8a4a24 100%)}
  .process{position:absolute;top:20px;left:16px;right:16px}
  .portrait__photo{top:168px;height:194px;background:linear-gradient(180deg,#e4ded8 0%,#b98c78 50%,#6a2532 100%)}
  .quote{position:absolute;left:0;right:0;bottom:0;height:210px;background:var(--rose);color:#fff;padding:14px 20px;text-align:center}
  .quote__mark{font-family:"Libre Baskerville",Georgia,serif;color:var(--gold-text);font-size:26px;line-height:1}
  .quote__text{font-style:italic;font-size:8px;line-height:1.45;margin-top:4px}
  .quote__by{margin-top:8px;color:var(--gold-text);font-size:9px;text-align:right}
</style>
</head>
<body>

<section class="sheet sheet--outside" aria-label="Brochure outside">
  <article class="panel flap">
    <div class="photo flap__photo" role="img" aria-label="Photo of a fountain pen nib"></div>
    <div class="flap__content">
      <h2 class="flap__title">Legal Solution Within Reach</h2>
      <div class="body-text">
        <p>Lorem Ipsum is simply dummy text of the printing and typesetting industry. Lorem Ipsum has been the industry's standard dummy text ever since the 1500s, when an unknown printer took a galley of type and scrambled it to make a type specimen book. It has survived not only five centuries, but also the leap into electronic typesetting, remaining essentially unchanged. It was popularised in the 1960s with the release of transfer sheets containing Lorem Ipsum passages, and more recently with layout programs including versions of Lorem Ipsum.</p>
        <p>Lorem Ipsum is simply dummy text of the printing and typesetting industry. Lorem Ipsum has been the industry's standard dummy text ever since the 1500s, when an unknown printer took a galley of type and scrambled it to make a type specimen book. It has survived not only five centuries, but also the leap into electronic typesetting, remaining essentially unchanged. It was popularised in the 1960s.</p>
      </div>
      <ul class="flap__list">
        <li>Lorem Ipsum is simply dummy text of the printing</li>
        <li>Lorem Ipsum is simply dummy text of the printing</li>
        <li>Lorem Ipsum is simply dummy text of the printing</li>
        <li>Lorem Ipsum is simply dummy text of the printing</li>
        <li>Lorem Ipsum is simply dummy text of the printing</li>
        <li>Lorem Ipsum is simply dummy text of the printing</li>
      </ul>
    </div>
    <footer class="flap__band"><span class="flap__url">www.hollins-legal.com</span></footer>
  </article>

  <article class="panel back">
    <div class="photo back__photo" role="img" aria-label="Silhouette of a Lady Justice statue against a blue sky"></div>
    <div class="back__block">
      <div class="brand"><span>HOLLINS</span><span class="brand__mark"></span><span>LEGAL, LLC</span></div>
      <address class="back__contact">
        48 Linden Row, Suite 3, Carver, MD 21000<br>
        Phone: (410) 555-0142 | Fax: (410) 555-0187<br>
        Email: dana@hollins-legal.com<br>
        www.hollins-legal.com
      </address>
    </div>
  </article>

  <article class="panel cover">
    <svg class="cover__art" width="247" height="572" viewBox="0 0 247 572" aria-hidden="true">
      <defs>
        <linearGradient id="coverTone" x1="0" y1="0" x2="1" y2="1">
          <stop offset="0" stop-color="#e9ddd0"/>
          <stop offset=".5" stop-color="#b3704a"/>
          <stop offset="1" stop-color="#7a3a22"/>
        </linearGradient>
      </defs>
      <path d="M0 0 H95 C210 60 240 250 150 400 C110 455 50 470 0 470 Z" fill="url(#coverTone)"/>
    </svg>
    <div class="photo" role="img" aria-label="Photo of a wooden judge's gavel" style="top:0;left:0;width:170px;height:460px"></div>
    <p class="cover__tagline">Estate Planning Special for <em>New Parents</em></p>
  </article>
</section>

<section class="sheet sheet--inside" aria-label="Brochure inside">
  <article class="panel">
    <div class="top-bar"></div>
    <div class="offer">
      <p class="offer__head">Estate Planning Special for New Parents</p>
      <p class="offer__price">$750 per couple</p>
      <p class="offer__who">For parents-to-be and parents<br>of children under 5 years old</p>
    </div>
    <div class="photo gavel__photo" role="img" aria-label="Photo of a gavel beside books and stacked coins"></div>
    <div class="red-block red-block--low body-text">
      <h3 class="q">Why should every parent have a will?</h3>
      <p>Imagine how many people love your children. Would there be a fight over who would care for your children if you passed away without leaving instructions?</p>
      <p>Naming a guardian in your will helps avoid litigation that would cause additional stress to your children and loved ones. You can also name a back-up in the event that your first choice is unable or unwilling to serve as guardian.</p>
      <h3 class="q">What happens if I die in Maryland without a will?</h3>
      <p>If you are married and have minor children, your spouse will inherit one half of your intestate property and your children will inherit the rest. If you have children but no spouse, your children will inherit everything.</p>
    </div>
  </article>

  <article class="panel">
    <div class="red-block red-block--high body-text">
      <p>For most parents, this plan doesn't make sense. Married people generally want their spouse to inherit all of their estate and unmarried people should have more control over how funds are distributed to their minor children.</p>
      <p>Furthermore, Maryland law doesn't take into account nontraditional families. For example, foster children and stepchildren that are not legally adopted will not automatically inherit a share of your estate.</p>
      <p>You can find the complete laws of intestacy (dying without a will) in the Maryland Code of Estates &amp; Trusts §§ 3-101 to 3-303.</p>
    </div>
    <div class="white-block body-text">
      <h3 class="q q--rose">Should we prepare a will now if we plan to have more children in the future?</h3>
      <p>There is no reason to put off drafting a will. A will can be written to treat your children as a "class" that would include any future children born to or adopted by you.</p>
      <h3 class="q q--rose">What does the estate planning package include?</h3>
      <p>Our estate planning package includes a will, an advance medical directive, and a power of attorney. A will names a guardian for your children and gives instructions on how to distribute your probate property at death. An advance medical directive, also known as a living will, states directions regarding your healthcare decisions in the event that you can't make those decisions yourself. A power of attorney gives someone the ability to handle your financial affairs during your lifetime.</p>
    </div>
    <div class="photo scales__photo" role="img" aria-label="Photo of brass scales of justice in front of law books"></div>
  </article>

  <article class="panel">
    <div class="top-bar" style="height:8px"></div>
    <div class="process body-text">
      <h3 class="q q--rose">How long will the process take?</h3>
      <p>Before our first meeting, you will receive information to help you start thinking about some of the decisions we will make during the initial consultation which lasts approximately one hour. It takes about 2 to 3 weeks after our initial meeting to draft your documents. You will receive draft copies of your documents to review before coming in for your last appointment to sign the documents in front of witnesses and a notary.</p>
    </div>
    <div class="photo portrait__photo" role="img" aria-label="Portrait photo of the firm's attorney"></div>
    <blockquote class="quote">
      <div class="quote__mark">&ldquo;</div>
      <p class="quote__text">"I've seen first-hand the problems created when a parent dies without a will. Young parents are least likely to think about estate planning, but having a plan for a guardian is most important when your children are small. I created our estate planning special to encourage new parents to start planning before it's too late."</p>
      <p class="quote__by">- Dana R. Hollins, Esq.</p>
    </blockquote>
  </article>
</section>

</body>
</html>
```